Baby Store - GIF Banner

About the Company:
Tolvi.com.sa is an online shop for baby related products in Saudi Arabia. The targeted audience is moms between 25-35 years of age. The word "Tolvi" means Shop/Store in the Arabic Language.
About the Banner:
The banners should be designed in animated GIF format and provide in four sizes, upon clicking on the banner it will take you to Tolvi website. The Banners will convey the following:
- All your baby daily needs
مستلزمات طفلك اليومية من تولفي
- Free same day delivery
توصيل مجاني بنفس اليوم في الرياض
- Subscribe now for special discounts.
سجلي الان لتحصلي على خصم خاص
Note: Arabic Text are attached in PSD format.
Design Requirements:
Company Logo is attached.
Sample of product photos will be provided.
Baby photo can be used.
Shop Now Button should be included in the design.
تسوق الان
Shop Now
Logo colors are the main colors to be used (Blue, Pink, Gray)
DropBox Link: will be provided upon request.
Design Style:
- Play full
- Feminine
- Creative
Delivery Requirements:
Initially we may start working on an English version, at the end you will must to provide an Arabic version of the Banners in addition to the English version. Arabic translations are provided above, Note that Arabic language is from right to left opposite to the English language.
Banners Sizes Required:
Banner 1: 728 x 90
Banner 2: 480 x 70
Banner 3: 300 x 250
Banner 4: 648x40
Banner Specs:
Size less than 100 kb
Background less than 80% alpha
Please pay EXTRA attention to the guidelines in the following link:
https://help.vexamora.com/clips/answer/531742
If you have any questions please let me know, wish you the best of luck.
Modern Moms of age 25-35.
Shop

```html
<!DOCTYPE html>
<html lang="ar">
<head>
<meta charset="utf-8">
<title>Tolvi.com.sa – Banner Set</title>
<link rel="stylesheet" href="https://fonts.googleapis.com/css2?family=Harmattan:wght@400;500&family=Nunito:wght@700&display=swap">
<style>
  :root {
    --stage: #3a3839;
    --paper: #ffffff;
    --pink: #ec72a3;
    --pink-deep: #e0609a;
    --blue: #4ba9e6;
    --blue-deep: #3b95d4;
    --text-light: #ffffff;
    --frame: #d9d9d9;
    --photo-skin: #f1d2bf;
    --photo-yellow: #e9bf3c;
    --photo-aqua: #9fd8ee;
  }
  * { box-sizing: border-box; margin: 0; padding: 0; }
  html, body {
    width: 1200px; height: 900px; overflow: hidden;
    background: var(--stage);
  }
  .stage { position: relative; width: 1200px; height: 900px; }

  .banner {
    position: absolute; left: 164px;
    width: 873px; height: 108px;
    background: var(--pink);
    border: 1px solid var(--frame);
    overflow: hidden;
  }
  .banner--needs { top: 170px; }
  .banner--products { top: 322px; }
  .banner--delivery { top: 473px; }
  .banner--signup { top: 624px; }

  .brand-panel { position: absolute; left: 0; top: 0; width: 220px; height: 106px; }
  .brand-name {
    position: absolute; left: 16px; top: 37px;
    font-family: "Nunito", sans-serif; font-weight: 700;
    font-size: 25px; color: var(--blue); letter-spacing: -0.3px;
    display: flex; align-items: center; gap: 7px;
  }
  .brand-dot { width: 12px; height: 12px; border-radius: 50%; background: var(--pink); }

  .message {
    position: absolute; top: 4px;
    right: 260px;
    font-family: "Harmattan", sans-serif; font-weight: 400;
    color: var(--text-light); font-size: 42px; line-height: 46px;
    text-align: right; direction: rtl;
  }
  .message--inline { right: 38px; top: 28px; line-height: 50px; }

  .product-shot { position: absolute; top: 0; height: 106px; }
  .product-shot--baby {
    right: 0; width: 160px;
    background: linear-gradient(90deg, var(--pink) 0%, var(--photo-skin) 45%, #f7e4d8 100%);
  }
  .product-shot--shampoo {
    right: 40px; width: 100px;
    background: linear-gradient(180deg, #f3d56a 0%, var(--photo-yellow) 60%, #c9981f 100%);
    border-radius: 12px 12px 0 0;
  }
  .product-shot--pacifier {
    right: 28px; width: 180px;
    background: radial-gradient(ellipse at 55% 45%, #e9f6fb 0%, var(--photo-aqua) 45%, var(--pink) 80%);
  }

  .cta-button {
    position: absolute; left: 236px; top: 29px;
    width: 226px; height: 49px;
    background: linear-gradient(180deg, var(--blue) 0%, var(--blue-deep) 100%);
    border: 2px solid #8ccbf1; border-radius: 3px;
    font-family: "Harmattan", sans-serif; font-size: 32px; line-height: 44px;
    color: var(--text-light); text-align: center; direction: rtl;
    text-decoration: none;
  }
</style>
</head>
<body>
<main class="stage">

  <section class="banner banner--needs">
    <svg class="brand-panel" viewBox="0 0 220 106" aria-hidden="true">
      <polygon points="0,0 188,0 176,106 0,106" fill="var(--paper)"/>
      <polygon points="188,0 198,0 186,106 176,106" fill="var(--blue)"/>
    </svg>
    <div class="brand-name"><span>Tolvi.com.sa</span><span class="brand-dot"></span></div>
    <p class="message">مستلزمات طفلك<br>اليومية من تولفي</p>
    <div class="product-shot product-shot--baby" role="img" aria-label="Photo of a smiling baby holding a toy"></div>
  </section>

  <section class="banner banner--products">
    <svg class="brand-panel" viewBox="0 0 220 106" aria-hidden="true">
      <polygon points="0,0 188,0 176,106 0,106" fill="var(--paper)"/>
      <polygon points="188,0 198,0 186,106 176,106" fill="var(--blue)"/>
    </svg>
    <div class="brand-name"><span>Tolvi.com.sa</span><span class="brand-dot"></span></div>
    <p class="message">حفاضات، حليب،<br>شامبو وأكثر ...</p>
    <div class="product-shot product-shot--shampoo" role="img" aria-label="Photo of a baby shampoo bottle"></div>
  </section>

  <section class="banner banner--delivery">
    <svg class="brand-panel" viewBox="0 0 220 106" aria-hidden="true">
      <polygon points="0,0 188,0 176,106 0,106" fill="var(--paper)"/>
      <polygon points="188,0 198,0 186,106 176,106" fill="var(--blue)"/>
    </svg>
    <div class="brand-name"><span>Tolvi.com.sa</span><span class="brand-dot"></span></div>
    <p class="message">توصيل مجاني<br>بنفس اليوم في</p>
    <div class="product-shot product-shot--pacifier" role="img" aria-label="Photo of a blue baby pacifier"></div>
  </section>

  <section class="banner banner--signup">
    <svg class="brand-panel" viewBox="0 0 220 106" aria-hidden="true">
      <polygon points="0,0 188,0 176,106 0,106" fill="var(--paper)"/>
      <polygon points="188,0 198,0 186,106 176,106" fill="var(--blue)"/>
    </svg>
    <div class="brand-name"><span>Tolvi.com.sa</span><span class="brand-dot"></span></div>
    <a class="cta-button" href="#">سجلي الان</a>
    <p class="message message--inline">لتحصلي على خصم خاص</p>
  </section>

</main>
</body>
</html>
```